KIVO Cosmetics LABELS

one good design wanted for the KIVO COSMETICS brand.

These are cosmetics and detergents. The labels should be about 3" wide and 4" deep. It must be colorful and interesting with some art on it. Flowers, girl, ? anything.

The word KIVO should guide your thinking a little.

It has to be bold and with striking colors. The attached images are there only as a guide of images we like and the logos are there, so you can see what we have already.

Ask any further questions please.

This design should be colorful and not finicky

Reason: Ready to work with any designer - through Brief Harbor - for other projects.

some intriguing graphics, images or something 'wow' is wanted in the designs

Those wanting something different and economic.

Cosmetics

• Each label in a range is to be the same 'ish and to allow space for the name of the individual product to be added; such as Seaweed Shampoo.

Use of the logo will be all labels but small in a corner, or ...

USE OF THE SHOWN IMAGES, SHOULD BE THERE BUT NOT PROMINENTLY

```html
<!DOCTYPE html>
<html lang="en">
<head>
<meta charset="utf-8">
<title>KIVO Cosmetics – Shampoo Label Range</title>
<link rel="stylesheet" href="https://fonts.googleapis.com/css2?family=Archivo:wght@300;400;900&display=swap">
<style>
  :root {
    --page-bg: #ffffff;
    --caption: #9a9a9a;
    --seaweed-bg-a: #dbe9e5;
    --seaweed-bg-b: #8fb5ab;
    --seaweed-art: #e0338f;
    --seaweed-name: #d3167f;
    --seaweed-sub: #f4c3dc;
    --almond-bg-a: #f2e6f2;
    --almond-bg-b: #b98fbf;
    --almond-art: #c9dd28;
    --almond-name: #4c9a32;
    --almond-sub: #e9d6ec;
    --aloe-bg-a: #fbfbc8;
    --aloe-bg-b: #d8dc2c;
    --aloe-art: #17a9e6;
    --aloe-name: #12a185;
    --aloe-sub: #9fd9b4;
  }
  * { box-sizing: border-box; margin: 0; padding: 0; }
  html, body {
    width: 1200px;
    height: 800px;
    overflow: hidden;
    background: var(--page-bg);
    font-family: "Archivo", Arial, sans-serif;
  }
  .sheet {
    position: relative;
    width: 1200px;
    height: 800px;
  }
  .sheet-caption {
    position: absolute;
    left: 36px;
    top: 36px;
    font-size: 12.5px;
    font-weight: 300;
    letter-spacing: 0.6px;
    color: var(--caption);
  }
  .label {
    position: absolute;
    top: 350px;
    width: 210px;
    height: 282px;
    overflow: hidden;
  }
  .label--seaweed { left: 207px; }
  .label--almond  { left: 503px; }
  .label--aloe    { left: 797px; }

  .label-art {
    position: absolute;
    inset: 0;
  }
  .label--seaweed .label-art {
    background:
      radial-gradient(circle at 50% 42%, var(--seaweed-art) 0 22%, transparent 40%),
      linear-gradient(90deg, var(--seaweed-bg-a), var(--seaweed-bg-b));
  }
  .label--almond .label-art {
    background:
      radial-gradient(circle at 42% 42%, var(--almond-art) 0 22%, transparent 40%),
      linear-gradient(90deg, var(--almond-bg-a), var(--almond-bg-b));
  }
  .label--aloe .label-art {
    background:
      radial-gradient(circle at 42% 42%, var(--aloe-art) 0 22%, transparent 40%),
      linear-gradient(90deg, var(--aloe-bg-a), var(--aloe-bg-b));
  }

  .product-name {
    position: absolute;
    left: 6px;
    top: 237px;
    font-size: 27px;
    font-weight: 900;
    line-height: 1;
    letter-spacing: -0.3px;
  }
  .product-type {
    position: absolute;
    left: 7px;
    top: 263px;
    font-size: 13px;
    font-weight: 300;
    line-height: 1;
  }
  .brand-name {
    position: absolute;
    right: 7px;
    top: 258px;
    font-size: 14px;
    font-weight: 900;
    line-height: 1;
  }
  .label--seaweed .product-name,
  .label--seaweed .brand-name { color: var(--seaweed-name); }
  .label--almond .product-name,
  .label--almond .brand-name  { color: var(--almond-name); }
  .label--aloe .product-name,
  .label--aloe .brand-name    { color: var(--aloe-name); }
  .label--seaweed .product-type { color: var(--seaweed-sub); }
  .label--almond .product-type  { color: var(--almond-sub); }
  .label--aloe .product-type    { color: var(--aloe-sub); }
</style>
</head>
<body>
<main class="sheet">
  <p class="sheet-caption">PROJECT KIVO COSMETICS LOGO / JUN 2013</p>

  <section class="label label--seaweed">
    <div class="label-art" role="img" aria-label="Bubble artwork in magenta and pink on a sea-green striped ground"></div>
    <h2 class="product-name">SEAWEED</h2>
    <p class="product-type">SHAMPOO</p>
    <p class="brand-name">KIVO</p>
  </section>

  <section class="label label--almond">
    <div class="label-art" role="img" aria-label="Bubble artwork in lime and yellow on a lilac striped ground"></div>
    <h2 class="product-name">ALMOND</h2>
    <p class="product-type">SHAMPOO</p>
    <p class="brand-name">KIVO</p>
  </section>

  <section class="label label--aloe">
    <div class="label-art" role="img" aria-label="Bubble artwork in sky blue and green on a yellow striped ground"></div>
    <h2 class="product-name">ALOE</h2>
    <p class="product-type">SHAMPOO</p>
    <p class="brand-name">KIVO</p>
  </section>
</main>
</body>
</html>
```